Postcard Design Project

Education- charter school- elementary k-6th grades- performing arts integrated in to the core curriculum

Industry/Entity Type

School

```html
<!DOCTYPE html>
<html lang="en">
<head>
<meta charset="utf-8">
<title>Bright Path Arts Community School – Enrollment Postcard</title>
<link rel="stylesheet" href="https://fonts.googleapis.com/css2?family=Didact+Gothic&family=Montserrat:wght@700&display=swap">
<style>
  :root {
    --paper: #ffffff;
    --ink: #111111;
    --rule: #6b6b6b;
    --brand-purple: #4b3c8f;
    --brand-violet: #5b4aa8;
    --panel-grey: #b9bcc4;
    --panel-sky: #8fc3e6;
    --panel-blue: #2f7fc4;
    --panel-sand: #c9b7a2;
    --panel-pink: #d46a9e;
    --panel-plum: #9a4d93;
  }
  * { margin: 0; padding: 0; box-sizing: border-box; }
  html, body {
    width: 1200px; height: 816px; overflow: hidden;
    background: var(--paper);
  }
  .postcard {
    position: relative; width: 1200px; height: 816px;
    background: var(--paper); color: var(--ink);
    font-family: "Didact Gothic", "Century Gothic", sans-serif;
  }
  .message-panel {
    position: absolute; left: 28px; top: 28px; width: 546px; height: 760px;
    overflow: hidden;
  }
  .panel-backdrop {
    position: absolute; inset: 0;
    background:
      radial-gradient(ellipse 60% 30% at 30% 10%, #d2d3d8 0%, transparent 70%),
      radial-gradient(ellipse 45% 40% at 85% 25%, var(--panel-blue) 0%, transparent 75%),
      radial-gradient(ellipse 50% 25% at 65% 15%, var(--panel-sky) 0%, transparent 75%),
      radial-gradient(ellipse 55% 25% at 35% 50%, var(--panel-sand) 0%, transparent 75%),
      radial-gradient(ellipse 50% 25% at 75% 65%, #7b6d98 0%, transparent 75%),
      radial-gradient(ellipse 60% 30% at 30% 78%, var(--panel-pink) 0%, transparent 75%),
      linear-gradient(180deg, var(--panel-grey) 0%, #a9c2d8 30%, #b3a9ad 55%, #c8709f 80%, var(--panel-plum) 100%);
  }
  .panel-copy { position: absolute; left: 32px; top: 0; width: 480px; }
  .headline {
    position: absolute; top: 50px; width: 470px;
    font-family: "Montserrat", "Arial", sans-serif; font-weight: 700;
    font-size: 29px; line-height: 34px;
  }
  .body-text {
    position: absolute; width: 470px;
    font-size: 20px; line-height: 24px;
  }
  .body-text.intro { top: 158px; }
  .body-text.amazed { top: 336px; }
  .body-text.meals { top: 396px; }
  .call-to-action {
    position: absolute; top: 480px; width: 480px;
    font-family: "Montserrat", "Arial", sans-serif; font-weight: 700;
    font-size: 18px; line-height: 24px;
  }
  .school-address {
    position: absolute; top: 624px; font-style: normal;
    font-family: "Montserrat", "Arial", sans-serif; font-weight: 700;
    font-size: 16px; line-height: 22px; text-transform: uppercase;
  }
  .school-mark {
    position: absolute; left: 612px; top: 150px; width: 330px;
    display: flex; align-items: center; gap: 10px; justify-content: center;
  }
  .school-mark .dot {
    width: 18px; height: 18px; border-radius: 50%; background: var(--brand-violet); flex: none;
  }
  .school-mark .name {
    font-size: 19px; color: var(--brand-purple); white-space: nowrap;
  }
  .stamp-box {
    position: absolute; left: 976px; top: 99px; width: 153px; height: 154px;
    border: 3px solid var(--ink); border-radius: 2px;
  }
  .address-lines { position: absolute; left: 612px; top: 0; }
  .address-lines span {
    position: absolute; left: 0; width: 515px; height: 1px; background: var(--rule);
  }
</style>
</head>
<body>
<div class="postcard">
  <section class="message-panel">
    <div class="panel-backdrop" role="img" aria-label="Softly blurred photo of children performing on stage in blue, beige and pink light"></div>
    <div class="panel-copy">
      <h1 class="headline">All grade levels take visual arts, music, drama, and dance.</h1>
      <p class="body-text intro">Small class sizes with Highly Qualified teachers in the core subjects, beautiful facilities with a five acre campus provide for an outdoor learning experience, and a dedicated staff committed to a positive learning environment are just a few reasons that</p>
      <p class="body-text amazed">you will be amazed by this performing arts community school.</p>
      <p class="body-text meals">Breakfast and lunch are provided at no cost to you! All of this tuition free! Please contact us for a tour of our school.</p>
      <p class="call-to-action">Classes fill up quickly so call today to ensure your child’s enrollment for the 2016-17 school year.</p>
      <address class="school-address">
        Bright Path Arts Community School<br>
        250 Maple Grove Road<br>
        Riverton, Ohio 43000<br>
        Phone (555) 010-4827
      </address>
    </div>
  </section>

  <div class="school-mark">
    <span class="dot"></span>
    <span class="name">Bright Path Arts Community School</span>
  </div>

  <div class="stamp-box"></div>

  <div class="address-lines">
    <span style="top:407px"></span>
    <span style="top:509px"></span>
    <span style="top:612px"></span>
    <span style="top:714px"></span>
  </div>
</div>
</body>
</html>
```